Hedge fund needs power point design for marketing pitch

We need a designer to make our power point pitch more aesthetically appealing to potential clients. We will be marketing our hedge fund to high net worth individuals and financial institutions. The ideal design will look professional and project confidence to our potential clients. We have attached a rough outline of what we have completed so far. We have also attached example cover pages for 2 pitch books produced by our competitors.

Target Market(s)

Financial institutions and wealthy investors

Industry/Entity Type

Finance

Requirements
Must have
• must use our logo and current slides. Must look professional

```html
<!DOCTYPE html>
<html lang="en">
<head>
<meta charset="utf-8">
<title>Aldermont Derivatives Fund LP</title>
<link rel="stylesheet" href="https://fonts.googleapis.com/css2?family=Jost:wght@300;400;600;700&family=Tinos&display=swap">
<style>
  :root {
    --charcoal: #312f30;
    --charcoal-light: #3a3839;
    --gold: #e2b840;
    --white: #ffffff;
    --ink: #1f1d1e;
  }
  * { margin: 0; padding: 0; box-sizing: border-box; }
  html, body { width: 1200px; height: 848px; overflow: hidden; background: var(--white); }
  .cover {
    position: relative;
    width: 1200px;
    height: 848px;
    background: var(--white);
    font-family: "Jost", "Futura", sans-serif;
    overflow: hidden;
  }
  .hero {
    position: absolute;
    left: 0; top: 0;
    width: 1200px; height: 505px;
    background: var(--charcoal);
    text-align: center;
    color: var(--white);
  }
  .fund-title {
    position: absolute;
    left: 0; right: 0; top: 125px;
    font-weight: 300;
    font-size: 74px;
    line-height: 76px;
    letter-spacing: 1px;
  }
  .fund-title strong { font-weight: 700; }
  .classification {
    position: absolute;
    left: 0; right: 0; top: 308px;
    font-weight: 300;
    font-size: 29px;
    color: var(--gold);
    letter-spacing: 0.5px;
  }
  .issue-date {
    position: absolute;
    left: 0; right: 0; top: 394px;
    font-weight: 300;
    font-size: 21px;
    display: flex;
    justify-content: center;
    align-items: center;
    gap: 12px;
  }
  .issue-date .marker {
    width: 11px; height: 11px;
    background: var(--gold);
    display: inline-block;
  }
  .web-band {
    position: absolute;
    left: 0; top: 505px;
    width: 1200px; height: 47px;
    background: var(--gold);
    color: var(--white);
    font-weight: 600;
    font-size: 21px;
    letter-spacing: 9px;
    text-align: center;
    line-height: 47px;
    box-shadow: 0 14px 16px -10px rgba(0,0,0,0.35);
  }
  .firm-name {
    position: absolute;
    left: 82px; top: 700px;
    color: var(--ink);
    font-weight: 400;
    line-height: 1;
  }
  .firm-name .primary {
    display: block;
    font-size: 50px;
    letter-spacing: 4px;
  }
  .firm-name .secondary {
    display: block;
    margin-top: 10px;
    font-size: 21px;
    letter-spacing: 1.2px;
  }
  .copyright {
    position: absolute;
    right: 32px; top: 802px;
    font-family: "Tinos", "Times New Roman", serif;
    font-size: 14px;
    color: var(--ink);
  }
</style>
</head>
<body>
  <main class="cover">
    <section class="hero">
      <h1 class="fund-title">ALDERMONT<br>DERIVATIVES FUND <strong>LP</strong></h1>
      <p class="classification">CONFIDENTIAL</p>
      <p class="issue-date"><span class="marker"></span>APRIL 2016<span class="marker"></span></p>
    </section>
    <div class="web-band">WWW.ALDERMONT.COM</div>
    <div class="firm-name">
      <span class="primary">ALDERMONT</span>
      <span class="secondary">CAPITAL MANAGEMENT LLC</span>
    </div>
    <p class="copyright">Copy right to Aldermont Capital Management LLC</p>
  </main>
</body>
</html>
```